Glimmorlo Frozen Yogurt

I am looking for a postcard to use for advertising purposes. We are a self serve frozen business that serves frozen yogurt, ice cream and gelato. We also have smoothies, milkshakes, waffle cones and waffle bowls. We have a bottoms bar and extensive toppings bar with only premium toppings and syrups.

Our main colors are purple, lime green and orange and the store is very
bright but not focused on kids, it is more trendy.

We have over 40 different candy, fruit and syrup toppings to choose from.
We give back to our community in many ways, as well as holding fundraising
for our local schools, churches and charities.

Target Market(s)

young and mature alike

Industry/Entity Type

Business

Font styles to use
Sans Serif

Colors
6b449b
add136
f37122

Requirements
Must have
• color, our colors are lime green, purple and orange.
Nice to have
• I would like to have some type of discount on there. Maybe a 20% off their purchase with the postcard.

```html
<!DOCTYPE html>
<html lang="en">
<head>
<meta charset="UTF-8">
<title>Glimmorlo Frozen Yogurt – Postcard</title>
<link href="https://fonts.googleapis.com/css2?family=Archivo:wght@600;700;800&display=swap" rel="stylesheet">
<style>
  :root {
    --purple: #5b2a86;
    --purple-dark: #3d1f5a;
    --beige: #e8e7d3;
    --lime: #add136;
    --orange: #f37122;
    --paper: #ffffff;
    --stage: #e3e3e3;
    --pink: #e78aa0;
  }
  * { box-sizing: border-box; margin: 0; padding: 0; }
  html, body { width: 1200px; height: 1200px; overflow: hidden; }
  body {
    background: var(--stage);
    font-family: "Archivo", "Helvetica Neue", Arial, sans-serif;
    position: relative;
  }
  .postcard {
    position: absolute;
    left: 210px;
    width: 780px;
    height: 530px;
    background: var(--paper);
    border-radius: 10px;
    overflow: hidden;
    box-shadow: 0 2px 6px rgba(0,0,0,0.12);
  }
  .postcard--front { top: 40px; }
  .postcard--back { top: 630px; }

  /* Front */
  .fruit-pattern { position: absolute; left: 600px; top: 220px; width: 180px; height: 310px; }
  .photo {
    position: absolute; left: 0; top: 0; width: 640px; height: 300px;
    background: linear-gradient(135deg, #8a9099 0%, #c9c9cf 30%, var(--pink) 55%, #d8707f 75%, #9b2232 100%);
  }
  .info-band { position: absolute; left: 0; top: 280px; width: 660px; height: 250px; }
  .ribbon {
    position: absolute; left: 250px; top: 262px; width: 220px; height: 42px;
    background: var(--purple);
    clip-path: polygon(0 0, 100% 0, 94% 50%, 100% 100%, 0 100%, 6% 50%);
    color: #fff; font-weight: 800; font-size: 20px; letter-spacing: 0.5px;
    display: flex; align-items: center; justify-content: center;
  }
  .brand {
    position: absolute; left: 36px; top: 354px; width: 300px; color: var(--purple);
    font-weight: 800; line-height: 1;
  }
  .brand__name { font-size: 44px; letter-spacing: 0.5px; white-space: nowrap; }
  .brand__sub { font-size: 28px; margin-top: 8px; white-space: nowrap; }
  .divider { position: absolute; left: 350px; top: 352px; width: 2px; height: 96px; background: var(--orange); }
  .contacts { position: absolute; left: 368px; top: 364px; list-style: none; color: var(--purple); font-weight: 700; font-size: 14px; }
  .contacts li { display: flex; align-items: center; gap: 8px; height: 24px; white-space: nowrap; }
  .contacts svg { width: 12px; height: 12px; flex: none; color: var(--purple); }

  /* Back */
  .rule-v { position: absolute; top: 0; width: 1.5px; height: 100%; background: var(--purple); }
  .rule-v--left { left: 24px; }
  .rule-v--mid { left: 420px; }
  .rule-v--right { left: 752px; }
  .write-lines { position: absolute; left: 46px; top: 62px; width: 350px; }
  .write-lines span { display: block; height: 40px; border-bottom: 1.5px dashed var(--purple); }
  .back-brand { position: absolute; left: 442px; top: 52px; color: var(--purple); font-weight: 800; line-height: 1.05; }
  .back-brand__name { font-size: 24px; }
  .back-brand__sub { font-size: 18px; }
  .back-brand__rule { width: 166px; height: 4px; background: var(--lime); margin-top: 8px; }
  .stamp { position: absolute; left: 612px; top: 86px; width: 112px; height: 112px; }
</style>
</head>
<body>

<section class="postcard postcard--front">
  <svg class="fruit-pattern" viewBox="0 0 180 310" role="img" aria-label="Decorative pattern of purple fruit silhouettes">
    <defs>
      <linearGradient id="fruitTone" x1="0" y1="0" x2="1" y2="1">
        <stop offset="0" stop-color="#efe9f4"/>
        <stop offset="1" stop-color="#b79ccf"/>
      </linearGradient>
    </defs>
    <polygon fill="url(#fruitTone)" points="20,0 180,0 180,310 20,310 0,298 20,286 0,274 20,262 0,250 20,238 0,226 20,214 0,202 20,190 0,178 20,166 0,154 20,142 0,130 20,118 0,106 20,94 0,82 20,70 0,58 20,46 0,34 20,22 0,10"/>
  </svg>

  <div class="photo" role="img" aria-label="Photo of two glasses of pink berry frozen yogurt with mint, raspberries, red currants and blueberries"></div>

  <svg class="info-band" viewBox="0 0 660 250" aria-hidden="true">
    <polygon fill="var(--beige)" points="0,10 10,0 20,10 30,0 40,10 50,0 60,10 70,0 80,10 90,0 100,10 110,0 120,10 130,0 140,10 150,0 160,10 170,0 180,10 190,0 200,10 210,0 220,10 230,0 240,10 250,0 260,10 270,0 280,10 290,0 300,10 310,0 320,10 330,0 340,10 350,0 360,10 370,0 380,10 390,0 400,10 410,0 420,10 430,0 440,10 450,0 460,10 470,0 480,10 490,0 500,10 510,0 520,10 530,0 540,10 550,0 560,10 570,0 580,10 590,0 600,10 610,0 620,10 630,0 640,10 660,0 660,250 0,250"/>
  </svg>

  <div class="ribbon">FRUIT YOGURT</div>

  <div class="brand">
    <div class="brand__name">GLIMMORLO</div>
    <div class="brand__sub">FROZEN YOGURT</div>
  </div>
  <div class="divider"></div>
  <ul class="contacts">
    <li>
      <svg viewBox="0 0 12 12"><path fill="currentColor" d="M6 0a4 4 0 0 0-4 4c0 3 4 8 4 8s4-5 4-8a4 4 0 0 0-4-4zm0 5.5A1.5 1.5 0 1 1 6 2.5a1.5 1.5 0 0 1 0 3z"/></svg>
      2158 Brookmere Ave Dunwell, Ohio
    </li>
    <li>
      <svg viewBox="0 0 12 12"><circle cx="6" cy="6" r="5" fill="currentColor"/></svg>
      Glimmorlo Frozen Yogurt
    </li>
    <li>
      <svg viewBox="0 0 12 12"><path fill="currentColor" d="M2.5 0.5l2 2.5-1.2 1.3c.7 1.6 2 2.9 3.4 3.6L8 6.6l2.5 2-1 2.4C5 11 1 7 1 2.5z"/></svg>
      +1 555-014-2287
    </li>
  </ul>
</section>

<section class="postcard postcard--back">
  <div class="rule-v rule-v--left"></div>
  <div class="rule-v rule-v--mid"></div>
  <div class="rule-v rule-v--right"></div>

  <div class="write-lines">
    <span></span><span></span><span></span><span></span><span></span>
    <span></span><span></span><span></span><span></span><span></span><span></span>
  </div>

  <div class="back-brand">
    <div class="back-brand__name">GLIMMORLO</div>
    <div class="back-brand__sub">FROZEN YOGURT</div>
    <div class="back-brand__rule"></div>
  </div>

  <svg class="stamp" viewBox="0 0 112 112" aria-hidden="true">
    <rect x="2" y="2" width="108" height="108" fill="none" stroke="var(--purple)" stroke-width="2"/>
    <path d="M12 30V12h18M82 12h18v18M100 82v18H82M30 100H12V82" fill="none" stroke="var(--orange)" stroke-width="3"/>
  </svg>
</section>

</body>
</html>
```